Landfill Gas-to-Renewable Natural Gas business

We have a website ( corvelmetharoutes .com via Net Burrow) that needs to be revamped.

We have three RNG projects in Puerto Rico (Humacao, Ponce, Salinas), that take landfill gas (LFG) and produce renewable liquid natural gas (R-LNG) for companies looking to offset their carbon emissions (footprint). We also produce a renewable carbon dioxide (R-CO2) that can be reused for industrial CO2 purposes. All CO2 is imported to the island, so reusing CO2 on the island further reduces global CO2 emissions. The design should reflect renewables, sustainability, professionalism, safety and experience in this sector.

Sites with RNG examples:
https://www.qx.com/en_us/united-states/home/what-we-do/production-and-operations/tolvane-fuels.html
https://brambleflowco.com/
http://kessfordpower.com/operations/
https://wyndcastle.com/
https://www.tamberhold.com/
https://pexloweco.com/
https://sandmoorbiolines.com/
https://curvetto.com/
https://www.dolvatri.com/renewable-natural-gas/
https://www.haskipowerworks.com/

Renewables Natural Gas, Sustainability,

4 page

• Health, Safety, Environment (HSE) aspect. Industry experience section, about us, photos, landfill gas, LNG, RNG, CO2

```html
<!DOCTYPE html>
<html lang="en">
<head>
<meta charset="utf-8">
<title>Corvel Energies — Island Sourced Waste-to-Energy</title>
<link rel="stylesheet" href="https://fonts.googleapis.com/css2?family=Cormorant+Garamond:wght@400;500;600&family=Merriweather:wght@700&family=Roboto:wght@400;500&family=Tinos:wght@400;700&display=swap">
<style>
:root{
  --blue:#1a63e0;
  --blue-dark:#124fc0;
  --green:#1fcf6b;
  --green-band:#22c560;
  --text:#333;
  --muted:#555;
  --white:#fff;
  --line:#d8dbe0;
}
*{box-sizing:border-box;margin:0;padding:0}
html,body{width:1200px;height:3870px;overflow:hidden;background:#fff}
body{font-family:"Roboto",sans-serif;color:var(--text);position:relative}
.abs{position:absolute}
.serif{font-family:"Cormorant Garamond",serif}
.nav-font{font-family:"Tinos",serif}

/* top bar */
.topbar{left:0;top:0;width:1200px;height:40px;background:var(--blue);color:#fff;font-size:14px}
.topbar .socials{left:112px;top:12px;display:flex;gap:8px}
.topbar .socials span{width:12px;height:12px;border-radius:50%;background:#fff;display:block}
.topbar .call{right:116px;top:11px;display:flex;align-items:center;gap:8px;font-size:14px}

/* hero */
.hero{left:0;top:40px;width:1200px;height:712px;background:linear-gradient(180deg,#5e8ca3 0%,#7d9a86 30%,#4f7a3e 60%,#3d6a2a 100%)}
.brand{display:flex;align-items:center;gap:12px}
.brand .mark{width:58px;height:58px;border-radius:50%;border:3px solid rgba(255,255,255,.9)}
.brand .name{font-family:"Roboto",sans-serif;font-weight:400;font-size:26px;line-height:26px;color:#fff}
.hero .brand{left:112px;top:55px}
.mainnav{left:593px;top:82px;display:flex;gap:30px;align-items:center;font-size:15px;color:#fff}
.btn{display:inline-flex;align-items:center;justify-content:center;border-radius:24px;color:#fff;font-family:"Tinos",serif;font-size:15px;text-transform:uppercase}
.mainnav .btn{background:var(--green);width:163px;height:44px;margin-left:-8px}
.hero h1{left:0;width:1200px;top:245px;text-align:center;font-family:"Merriweather",serif;font-weight:700;font-size:54px;color:#fff}
.hero .sub{left:0;width:1200px;top:322px;text-align:center;font-family:"Tinos",serif;font-size:30px;color:#fff;letter-spacing:.5px}
.hero .btn{left:507px;top:378px;width:185px;height:46px;background:var(--blue);font-weight:700;font-size:18px}
.green-rule{left:0;top:750px;width:1200px;height:9px;background:var(--green)}

/* service cards */
.card-img{width:300px;height:297px;top:676px}
.card-img.c1{left:111px;background:linear-gradient(180deg,#9fb6c9,#c99d6a 55%,#5a5550)}
.card-img.c2{left:449px;background:linear-gradient(180deg,#c0c5cc,#8e9096 60%,#5d6066)}
.card-img.c3{left:787px;background:linear-gradient(160deg,#3b9aa8,#2e6f7d 50%,#6a8f5f)}
.card-edge{width:28px;height:10px;top:963px}
.card{top:893px;width:275px;height:245px;background:#fff;box-shadow:0 2px 8px rgba(0,0,0,.12);padding:62px 26px 0}
.card h3{font-family:"Cormorant Garamond",serif;font-weight:600;font-size:20px;line-height:25px;color:#222}
.card p{font-size:13px;line-height:20px;color:var(--muted);margin-top:14px}
.card .arrow{position:absolute;left:28px;top:203px;width:56px;height:24px;border-radius:12px;display:flex;align-items:center;justify-content:center}
.icon-circle{width:100px;height:100px;border-radius:50%;border:5px solid #fff;display:flex;align-items:center;justify-content:center}

/* about */
.portrait-ring{left:112px;top:1245px;width:445px;height:445px;border-radius:50%;border:1.5px solid var(--green)}
.portrait-ring2{left:130px;top:1243px;width:427px;height:427px;border-radius:50%;border:1.5px solid var(--blue)}
.portrait{left:140px;top:1270px;width:412px;height:412px;border-radius:50%;background:radial-gradient(circle at 50% 40%,#b9a89a,#6f6a66 55%,#2d3136);border-bottom:8px solid var(--green)}
.eyebrow{display:flex;align-items:center;gap:8px;color:var(--blue);font-size:18px;font-weight:500;text-transform:uppercase}
.eyebrow i{display:block;width:33px;height:2px;background:var(--blue)}
.about .eyebrow{left:613px;top:1236px}
.about h2{left:611px;top:1264px;font-family:"Cormorant Garamond",serif;font-weight:500;font-size:36px;color:var(--green)}
.about .body{left:613px;top:1332px;width:480px;font-size:13.4px;line-height:23px;color:var(--muted)}
.about .body p+p{margin-top:23px}
.about .btn{left:617px;top:1694px;width:168px;height:45px;background:var(--blue)}

/* process */
.process{left:0;top:1784px;width:1200px;height:580px;background:var(--green-band)}
.process h2{left:557px;top:30px;width:630px;font-family:"Cormorant Garamond",serif;font-weight:500;font-size:35px;line-height:46px;color:#fff}
.process .btn{left:560px;top:186px;width:171px;height:41px;border:2px solid #fff;font-size:15px}
.illus-a{left:0;top:136px;width:557px;height:444px;background:linear-gradient(180deg,rgba(255,255,255,0) 0%,rgba(60,140,70,.35) 55%,#8a4a28 75%,#7a3f22)}
.illus-b{left:557px;top:260px;width:643px;height:320px;background:linear-gradient(180deg,rgba(255,255,255,0) 0%,rgba(60,140,70,.35) 45%,#8a4a28 70%,#7a3f22)}

/* faq */
.faq{left:0;top:2364px;width:1200px;height:640px;background:linear-gradient(180deg,#e9eef3,#f3f5f8 45%,#dfe6ee)}
.faq .eyebrow{left:0;width:1200px;top:52px;justify-content:center}
.faq h2{left:0;width:1200px;top:76px;text-align:center;font-family:"Cormorant Garamond",serif;font-weight:500;font-size:36px;color:var(--green)}
.qa{left:248px;width:703px;background:#fff;border:1px solid #e2e5ea;box-shadow:0 1px 3px rgba(0,0,0,.06)}
.qa .q{height:60px;display:flex;align-items:center;padding-left:18px;font-family:"Cormorant Garamond",serif;font-size:17px;color:#555}
.qa .q b{font-weight:600;font-size:20px;margin-right:6px;color:#444}
.qa .tog{position:absolute;right:4px;top:6px;width:28px;height:48px;border:1px solid #e0e0e0;display:flex;align-items:center;justify-content:center;background:#fff}
.qa .tog.open{background:var(--blue);border-color:var(--blue)}
.qa .a{margin:0 8px 8px;background:#f6f7f9;padding:14px 16px;font-size:12.5px;line-height:21px;color:#555}
.faq .btn{left:517px;top:544px;width:168px;height:44px;background:var(--green)}

/* contact */
.contact{left:0;top:3004px;width:1200px;height:580px;background:#fff}
.map{left:160px;top:40px;width:900px;height:480px;background:radial-gradient(ellipse at 50% 50%,#f2f3f5,#fff 70%)}
.contact .eyebrow{left:578px;width:421px;top:91px;justify-content:center}
.contact h2{left:578px;width:421px;top:116px;text-align:center;font-family:"Cormorant Garamond",serif;font-weight:500;font-size:36px;color:var(--green)}
.field{left:578px;width:421px;border:1px solid var(--line);background:#fff;font-size:14px;color:#555;padding:9px 14px}
.contact .btn{left:701px;top:448px;width:175px;height:48px;background:var(--green)}

/* footer */
.footer{left:0;top:3584px;width:1200px;height:286px;background:var(--blue)}
.footer .brand{left:503px;top:36px}
.footnav{left:0;width:1200px;top:139px;display:flex;justify-content:center;gap:26px;color:#fff;font-size:15px}
.social{top:178px;width:40px;height:40px;border-radius:50%;border:2px solid #fff}
.social.on{border-color:var(--green)}
.copy{left:0;width:1200px;top:247px;text-align:center;color:#fff;font-size:14px}
</style>
</head>
<body>

<header class="abs topbar">
  <div class="abs socials"><span></span><span></span><span></span></div>
  <div class="abs call">
    <svg width="12" height="12" viewBox="0 0 24 24"><path fill="#fff" d="M6.6 10.8a15 15 0 0 0 6.6 6.6l2.2-2.2c.3-.3.7-.4 1-.2 1.1.4 2.3.6 3.6.6.6 0 1 .4 1 1V20c0 .6-.4 1-1 1A17 17 0 0 1 3 4c0-.6.4-1 1-1h3.5c.6 0 1 .4 1 1 0 1.3.2 2.5.6 3.6.1.3 0 .7-.2 1z"/></svg>
    CALL US : 000.000.0000
  </div>
</header>

<section class="abs hero" role="img" aria-label="Aerial photo of a waste-to-energy plant among green fields">
  <div class="abs brand"><span class="mark"></span><span class="name">Corvel<br>Energies</span></div>
  <nav class="abs mainnav nav-font">
    <span>HOME</span><span>ABOUT</span><span>FAQ</span><span>CONTACT</span>
    <span class="btn">Get in touch</span>
  </nav>
  <h1 class="abs">Corvel Energies</h1>
  <div class="abs sub">ISLAND SOURCED WASTE-TO-ENERGY</div>
  <span class="abs btn">Get in touch</span>
</section>
<div class="abs green-rule"></div>

<!-- services -->
<div class="abs card-img c1" role="img" aria-label="Landfill gas facility at sunset"></div>
<div class="abs card-img c2" role="img" aria-label="Natural gas production plant"></div>
<div class="abs card-img c3" role="img" aria-label="Aerial view of waste processing tanks"></div>
<div class="abs card-edge" style="left:111px;background:var(--blue)"></div>
<div class="abs card-edge" style="left:449px;background:var(--green)"></div>
<div class="abs card-edge" style="left:787px;background:var(--blue)"></div>

<article class="abs card" style="left:136px">
  <h3>Landfill Gas-to-RNG &amp;<br>Electricity Facilities</h3>
  <p>We harness the power of landfill gas and convert it into renewable natural gas and clean electricity.</p>
  <span class="arrow" style="background:var(--blue)"><svg width="26" height="12" viewBox="0 0 26 12"><path d="M1 6h22M18 1l5 5-5 5" stroke="#fff" stroke-width="2" fill="none"/></svg></span>
</article>
<article class="abs card" style="left:474px">
  <h3>Renewable Natural Gas<br>Production</h3>
  <p>We contribute to a more sustainable future by producing RNG, a low -carbon alternative fuel.</p>
  <span class="arrow" style="background:var(--green)"><svg width="26" height="12" viewBox="0 0 26 12"><path d="M1 6h22M18 1l5 5-5 5" stroke="#fff" stroke-width="2" fill="none"/></svg></span>
</article>
<article class="abs card" style="left:812px">
  <h3>Advanced Waste Processing</h3>
  <p>Our facilities are equipped to capture and utilize waste emissions for energy production, minimizing environmental impact.</p>
  <span class="arrow" style="background:var(--blue)"><svg width="26" height="12" viewBox="0 0 26 12"><path d="M1 6h22M18 1l5 5-5 5" stroke="#fff" stroke-width="2" fill="none"/></svg></span>
</article>
<div class="abs icon-circle" style="left:298px;top:845px;background:var(--blue)">
  <svg width="44" height="48" viewBox="0 0 44 48" fill="none" stroke="#fff" stroke-width="2.5"><rect x="8" y="6" width="22" height="38" rx="2"/><rect x="13" y="12" width="12" height="8"/><path d="M30 16h6v22a3 3 0 0 1-6 0"/></svg>
</div>
<div class="abs icon-circle" style="left:636px;top:845px;background:var(--green)">
  <svg width="48" height="48" viewBox="0 0 48 48" fill="none" stroke="#fff" stroke-width="3"><path d="M38 16a17 17 0 1 1-10-7"/><path d="M24 14c5 6 6 9 6 12a6 6 0 0 1-12 0c0-3 2-6 6-12z" fill="#fff"/></svg>
</div>
<div class="abs icon-circle" style="left:974px;top:845px;background:var(--blue)">
  <svg width="50" height="46" viewBox="0 0 50 46" fill="none" stroke="#fff" stroke-width="2.5"><path d="M18 8l7-4 7 10M38 18l6 11-7 10h-8M15 38H7L2 28l7-12"/><path d="M29 14l3 0 0-4M29 40l-3-3 3-3M9 16l0 4-4 0"/></svg>
</div>

<!-- about -->
<section class="about">
  <div class="abs portrait-ring"></div>
  <div class="abs portrait-ring2"></div>
  <div class="abs portrait" role="img" aria-label="Portrait of the company president"></div>
  <div class="abs eyebrow"><i></i>About us</div>
  <h2 class="abs">I'am Daniel Moravec</h2>
  <div class="abs body">
    <p>Reputable United States Marine, General Manager and President, with experience extending more than 24 years of leadership over complete lifecycle of multi-million-dollar operations within the biogas and wastewa ter treatment space. Experienced in raising both debt and equity, Mr. Moravec offers leadership, technical, operational, and strategic expertise in senior-level administration, media and public relations, business develop ment, operational planning, client management as well as a reputation for having a keen under-standing and appreciation for cultural diversity, equity and equality.</p>
    <p>Serving in the United States Marine Corps, Daniel deployed three times &amp; is a combat veteran of Operations Enduring Freedom and Iraqi Freedom. He has received numerous awards and citations, including Presidential Unit Citation. Daniel holds a B.S. from Harlow Crest University and an MBA from The University of Westmarch.</p>
  </div>
  <span class="abs btn">Read more</span>
</section>

<!-- process -->
<section class="abs process">
  <div class="abs illus-a" role="img" aria-label="Illustration of landfill wells, gas separation and power generation"></div>
  <div class="abs illus-b" role="img" aria-label="Illustration of RNG delivery to industrial and commercial customers"></div>
  <h2 class="abs">Corvel Energies will Produce RenewableNatural Gas, Renewable CO2 and Power from Landfill Gas</h2>
  <span class="abs btn">Learn more</span>
</section>

<!-- faq -->
<section class="abs faq" role="img" aria-label="Faded photo of an LNG carrier ship">
  <div class="abs eyebrow"><i></i>Our FAQ<i></i></div>
  <h2 class="abs">Frequently Asked Questions</h2>
  <div class="abs qa" style="top:155px"><div class="q"><b>Q.</b> How long does it take to go from concept to project complete?</div>
    <span class="tog"><svg width="12" height="8" viewBox="0 0 12 8"><path d="M1 1l5 5 5-5" stroke="#555" stroke-width="1.5" fill="none"/></svg></span></div>
  <div class="abs qa" style="top:227px"><div class="q"><b>Q.</b> How are your projects financed?</div>
    <span class="tog"><svg width="12" height="8" viewBox="0 0 12 8"><path d="M1 1l5 5 5-5" stroke="#555" stroke-width="1.5" fill="none"/></svg></span></div>
  <div class="abs qa" style="top:299px"><div class="q"><b>Q.</b> What is Corvel Energies' business objective?</div>
    <span class="tog open"><svg width="12" height="8" viewBox="0 0 12 8"><path d="M1 7l5-5 5 5" stroke="#fff" stroke-width="1.5" fill="none"/></svg></span>
    <div class="a">Unlike some of our competitors, Corvel Energies' objective is to buy and hold assets for a long time, generally 20 years or longer.&nbsp; This assures our partners, relationship stability.</div></div>
  <div class="abs qa" style="top:452px"><div class="q"><b>Q.</b> How long does it take to go from concept to project complete?</div>
    <span class="tog"><svg width="12" height="8" viewBox="0 0 12 8"><path d="M1 1l5 5 5-5" stroke="#555" stroke-width="1.5" fill="none"/></svg></span></div>
  <span class="abs btn">Read more</span>
</section>

<!-- contact -->
<section class="abs contact">
  <div class="abs map" role="img" aria-label="Faint world map background"></div>
  <div class="abs eyebrow"><i></i>Get in touch<i></i></div>
  <h2 class="abs">Contact Us</h2>
  <div class="abs field" style="top:182px;height:38px">Name :</div>
  <div class="abs field" style="top:230px;height:38px">Email :</div>
  <div class="abs field" style="top:279px;height:38px">Phone :</div>
  <div class="abs field" style="top:329px;height:90px">Message :</div>
  <span class="abs btn">Send</span>
</section>

<!-- footer -->
<footer class="abs footer">
  <div class="abs brand"><span class="mark"></span><span class="name">Corvel<br>Energies</span></div>
  <nav class="abs footnav nav-font"><span>HOME</span><span>|</span><span>ABOUT</span><span>|</span><span>FAQ</span><span>|</span><span>CONTACT</span></nav>
  <span class="abs social" style="left:507px"></span>
  <span class="abs social on" style="left:557px"></span>
  <span class="abs social" style="left:606px"></span>
  <span class="abs social" style="left:654px"></span>
  <div class="abs copy">©2025 Corvel Energies. All rights reserved.</div>
</footer>

</body>
</html>
```